Kelby roamer wrap

I am currently;y looking to wrap my new 2019 for roamer 250. Im looking to have a nice high end looking wrap but Id like to keep it looking somewhat like the current vans to keep the fleet appearance. its the high top long version Ill include its picture as well

```html
<!DOCTYPE html>
<html lang="en">
<head>
<meta charset="utf-8">
<title>Kelby roamer 250 wrap – Tidewell Pool Service</title>
<link href="https://fonts.googleapis.com/css2?family=Lato:ital,wght@0,400;0,700;0,900;1,700&display=swap" rel="stylesheet">
<style>
  :root {
    --navy: #1f3a6e;
    --ocean: #1591bf;
    --ocean-light: #7fd0ee;
    --orange: #e2642a;
    --band-grey: #a9a9ad;
    --body-white: #ffffff;
    --page: #f4f4f4;
    --outline: #d6d6d6;
  }
  * { margin: 0; padding: 0; box-sizing: border-box; }
  html, body { width: 1200px; height: 1109px; overflow: hidden; background: var(--page); }
  .canvas { position: relative; width: 1200px; height: 1109px; font-family: "Lato", sans-serif; }
  .wrap-panel { position: absolute; left: 24px; width: 1152px; height: 416px; }
  .wrap-panel--driver { top: 40px; }
  .wrap-panel--passenger { top: 600px; }
  .wrap-panel svg { display: block; width: 100%; height: 100%; }
  .phone { font-weight: 900; font-size: 36px; fill: var(--navy); }
  .web { font-weight: 700; font-style: italic; font-size: 23px; fill: var(--navy); }
  .service-type { font-weight: 400; font-size: 15px; fill: var(--navy); }
  .tagline { font-weight: 700; font-size: 14.5px; fill: #fff; letter-spacing: 0.1px; }
  .brand-name { font-weight: 900; font-size: 30px; fill: var(--navy); }
  .brand-web { font-weight: 700; font-size: 10px; fill: var(--navy); letter-spacing: 1px; }
</style>
</head>
<body>
<div class="canvas">

  <!-- Driver side -->
  <section class="wrap-panel wrap-panel--driver">
    <svg viewBox="0 0 1152 416" xmlns="http://www.w3.org/2000/svg">
      <defs>
        <linearGradient id="waterDriver" x1="0" y1="1" x2="1" y2="0">
          <stop offset="0" stop-color="var(--ocean)"/>
          <stop offset="0.5" stop-color="var(--ocean-light)"/>
          <stop offset="1" stop-color="var(--ocean)"/>
        </linearGradient>
      </defs>
      <rect class="body" x="0" y="0" width="1152" height="416" rx="40" fill="var(--body-white)" stroke="var(--outline)"/>
      <path class="swoosh-blue" d="M930 0 L1130 0 Q1152 0 1152 30 L1152 300 L700 350 C520 370 390 385 280 392 L280 380 C610 310 830 190 930 0 Z" fill="var(--ocean)"/>
      <path class="water-splash" role="img" aria-label="Splashing pool water" d="M440 360 C600 320 760 260 860 200 L900 250 L880 340 L560 372 Z" fill="url(#waterDriver)" opacity="0.85"/>
      <path class="stripe-orange" d="M905 0 L935 0 C860 150 700 240 490 280 L488 272 C680 228 830 140 905 0 Z" fill="var(--orange)"/>
      <path class="stripe-orange-lower" d="M816 326 L1118 236 L1118 262 L840 328 Z" fill="var(--orange)"/>
      <path class="stripe-navy" d="M830 332 L1118 266 L1118 270 L836 336 Z" fill="var(--navy)"/>
      <path class="tagline-band" d="M280 340 L856 336 L856 372 L280 380 Z" fill="var(--band-grey)" opacity="0.9"/>
      <text class="tagline" x="304" y="363">OPENING/CLOSING &amp; WEEKLY SERVICING . SPECIALIZING IN GUNITE POOLS</text>
      <text class="phone" x="484" y="110">401-555-0148</text>
      <text class="web" x="484" y="142">www.PoolCrewRI.com</text>
      <text class="service-type" x="484" y="168">Commercial &amp; Residential</text>
      <g class="brand">
        <circle cx="968" cy="96" r="36" fill="var(--navy)"/>
        <text class="brand-name" x="968" y="170" text-anchor="middle">Tidewell</text>
        <text class="brand-name" x="968" y="204" text-anchor="middle">Pool Service</text>
        <text class="brand-web" x="968" y="232" text-anchor="middle">WWW.POOLCREWRI.COM</text>
      </g>
    </svg>
  </section>

  <!-- Passenger side -->
  <section class="wrap-panel wrap-panel--passenger">
    <svg viewBox="0 0 1152 416" xmlns="http://www.w3.org/2000/svg">
      <defs>
        <linearGradient id="waterPassenger" x1="1" y1="1" x2="0" y2="0">
          <stop offset="0" stop-color="var(--ocean)"/>
          <stop offset="0.5" stop-color="var(--ocean-light)"/>
          <stop offset="1" stop-color="var(--ocean)"/>
        </linearGradient>
      </defs>
      <rect class="body" x="0" y="0" width="1152" height="416" rx="40" fill="var(--body-white)" stroke="var(--outline)"/>
      <g class="graphics" transform="translate(1152 0) scale(-1 1)">
        <path class="swoosh-blue" d="M930 0 L1130 0 Q1152 0 1152 30 L1152 300 L700 350 C520 370 390 385 200 392 L200 380 C610 310 830 190 930 0 Z" fill="var(--ocean)"/>
        <path class="water-splash" role="img" aria-label="Splashing pool water" d="M380 360 C600 320 760 260 860 200 L900 250 L880 340 L520 372 Z" fill="url(#waterPassenger)" opacity="0.85"/>
        <path class="stripe-orange" d="M870 0 L930 0 C850 150 700 250 470 295 L466 285 C680 238 800 140 870 0 Z" fill="var(--orange)"/>
        <path class="stripe-orange-lower" d="M850 328 L1118 248 L1118 274 L874 330 Z" fill="var(--orange)"/>
        <path class="stripe-navy" d="M860 334 L1118 278 L1118 282 L866 338 Z" fill="var(--navy)"/>
        <path class="tagline-band" d="M250 340 L856 336 L856 372 L250 380 Z" fill="var(--band-grey)" opacity="0.9"/>
      </g>
      <text class="tagline" x="336" y="363">OPENING/CLOSING &amp; WEEKLY SERVICING . SPECIALIZING IN GUNITE POOLS</text>
      <text class="phone" x="668" y="110" text-anchor="end">401-555-0148</text>
      <text class="web" x="668" y="142" text-anchor="end">www.PoolCrewRI.com</text>
      <text class="service-type" x="668" y="168" text-anchor="end">Commercial &amp; Residential</text>
      <g class="brand">
        <circle cx="184" cy="96" r="36" fill="var(--navy)"/>
        <text class="brand-name" x="184" y="170" text-anchor="middle">Tidewell</text>
        <text class="brand-name" x="184" y="204" text-anchor="middle">Pool Service</text>
        <text class="brand-web" x="184" y="232" text-anchor="middle">WWW.POOLCREWRI.COM</text>
      </g>
    </svg>
  </section>

</div>
</body>
</html>
```